Selkirk Boat Lines and Freight Business Card

I need business cards for my new water taxi and freight transport business I have started here in Kodiak Alaska. Kodiak is a remote island in the middle of the gulf of Alaska. There are seven native villages around the island and Kodiak is the #2 fishing port in the United States. We also have the largest Seaward Corps Base in the U.S. My company will be providing water taxi and freight transport logistics to the villages and many hunting and fishing lodges as well as remote properties around the island.

I would like a business card that isn't status quo, something that stands out, either in feel or appearance. I do like clean minimal designs but it needs to have the necessary contact info on it.

Target Market(s)

remote lodge / property owners, residents of the many villages around Kodiak and any one wanting to enjoy the great outdoors of Kodiak Alaska

Industry/Entity Type

Business

Contact Information for Business Card

I like clean simple designs that aren't cluttered but still provide the necessary information

Colors
0255a3
3277b5
33a4d5
9bcb3c
add136
fbed22
ffc214
f78f20
f37122

Requirements
Must have
• logo and contact info
• Captain Marcus Hollend
• www.selkirkboatlines.com
• marcus@selkirkboatlines.com

```html
<!DOCTYPE html>
<html lang="en">
<head>
<meta charset="utf-8">
<title>Selkirk Boat Lines and Freight – Business Card</title>
<link rel="stylesheet" href="https://fonts.googleapis.com/css2?family=Montserrat:wght@400;600;700&display=swap">
<style>
  :root {
    --navy: #0255a3;
    --mid-blue: #3277b5;
    --sky: #33a4d5;
    --orange: #f78f20;
    --ink: #2b2b2b;
    --card: #ffffff;
    --backdrop: #e9e6e2;
  }
  html, body {
    margin: 0;
    width: 1200px;
    height: 1000px;
    overflow: hidden;
    background: var(--backdrop);
    font-family: "Montserrat", Arial, sans-serif;
  }
  .canvas { position: relative; width: 1200px; height: 1000px; }
  .card {
    position: absolute;
    left: 265px;
    width: 665px;
    height: 397px;
    background: var(--card);
    border-radius: 22px;
    overflow: hidden;
    box-shadow: 0 2px 6px rgba(0,0,0,0.15);
  }
  .card--front { top: 73px; }
  .card--back { top: 533px; }

  .brand {
    position: absolute;
    display: flex;
    flex-direction: column;
    align-items: center;
    text-align: center;
  }
  .brand__dot {
    width: 46px;
    height: 46px;
    border-radius: 50%;
    background: var(--orange);
    margin-bottom: 18px;
  }
  .brand__name {
    color: var(--navy);
    font-weight: 700;
    line-height: 1.15;
    margin: 0;
  }
  .card--front .brand { left: 38px; top: 150px; width: 290px; }
  .card--front .brand__name { font-size: 27px; }
  .card--back .brand { left: 0; right: 0; top: 154px; }
  .card--back .brand__dot { width: 56px; height: 56px; margin-bottom: 22px; }
  .card--back .brand__name { font-size: 36px; }

  .contact { position: absolute; left: 391px; top: 115px; }
  .contact__name {
    margin: 0;
    color: var(--navy);
    font-weight: 700;
    font-size: 21px;
  }
  .contact__role {
    margin: 6px 0 0;
    color: var(--ink);
    font-size: 14px;
  }
  .contact__list { list-style: none; margin: 40px 0 0; padding: 0; }
  .contact__item {
    display: flex;
    align-items: center;
    gap: 8px;
    color: var(--ink);
    font-size: 14.5px;
    margin-bottom: 11px;
  }
  .contact__icon { width: 15px; height: 15px; flex: none; }

  .footer-band {
    position: absolute;
    left: 0;
    right: 0;
    bottom: 0;
    height: 80px;
    background: linear-gradient(to bottom, var(--navy), var(--sky));
  }
</style>
</head>
<body>
<main class="canvas">

  <section class="card card--front">
    <div class="brand">
      <span class="brand__dot"></span>
      <p class="brand__name">Selkirk Boat Lines<br>and Freight</p>
    </div>

    <div class="contact">
      <h1 class="contact__name">Marcus Hollend</h1>
      <p class="contact__role">Captain</p>
      <ul class="contact__list">
        <li class="contact__item">
          <svg class="contact__icon" viewBox="0 0 16 16" aria-hidden="true">
            <rect x="1" y="3" width="14" height="10" rx="1" fill="#f78f20"/>
            <path d="M1.5 3.8 L8 9 L14.5 3.8" fill="none" stroke="#fff" stroke-width="1.2"/>
          </svg>
          marcus@selkirkboatlines.com
        </li>
        <li class="contact__item">
          <svg class="contact__icon" viewBox="0 0 16 16" aria-hidden="true">
            <circle cx="8" cy="8" r="6.5" fill="none" stroke="#f78f20" stroke-width="1.6"/>
            <path d="M7 6 L13 11 L10.2 11.2 L11.6 14 L10.4 14.6 L9 11.8 L7 13.6 Z" fill="#f78f20"/>
          </svg>
          www.selkirkboatlines.com
        </li>
      </ul>
    </div>

    <div class="footer-band" role="img" aria-label="Decorative blue wave band along the bottom edge"></div>
  </section>

  <section class="card card--back">
    <div class="brand">
      <span class="brand__dot"></span>
      <p class="brand__name">Selkirk Boat Lines<br>and Freight</p>
    </div>
  </section>

</main>
</body>
</html>
```